Quillmere Financial Plans

I am looking for a complete resdesign of my small financial presentation. This is a Word Doc/PDF that I print off when meeting with people in private. I often present my "two pager" that I have been using for years and years. It tells them the basics of what I do, how I help people and foundational financial principles.

I have recently gone out on my own in business and have completely rebranded. This presentation is my most used tool, so it is the first of many things I would like to redo. I am hoping it will somehow coordinate with the colors of my business, not necessarily the EXACT same 3 colors everywhere, but have the design colors compliment.

I've uploaded all my logo designs, as well as the current "two-pager". I am not against it going to 3 pages if needed. As it will still land on 2 pages with duplex printing.

It has always been VERY simple. I am wanting it built into a more professional and design specific format, to show off my branding, without being over cluttered.

I am completely open to ANY graphics changes. Obviously some are very novice, the house on the last page has always been overly simplified.

```html
<!DOCTYPE html>
<html lang="en">
<head>
<meta charset="utf-8">
<title>Quillmere Financial Plans – Growth &amp; Taxes</title>
<link rel="stylesheet" href="https://fonts.googleapis.com/css2?family=Arimo:wght@400;700&family=Libre+Baskerville:wght@700&display=swap">
<style>
  :root {
    --leaf: #92d050;
    --mint: #e2efda;
    --brand-green: #00b050;
    --forest: #2d5a1e;
    --ink: #111111;
    --night: #000000;
    --brick: #8b0e0e;
    --paper: #ffffff;
  }
  * { box-sizing: border-box; margin: 0; padding: 0; }
  html, body { width: 927px; height: 1200px; overflow: hidden; background: var(--paper); }
  body { position: relative; font-family: "Arimo", Arial, sans-serif; color: var(--ink); }

  .doubling-table { position: absolute; top: 108px; border-collapse: collapse; font-size: 14px; }
  .doubling-table th {
    background: var(--leaf); font-size: 17px; font-weight: 700; height: 23px;
    padding: 0 8px; text-align: left; line-height: 23px;
  }
  .doubling-table th.rate { text-align: right; }
  .doubling-table td { height: 22.6px; padding: 0 8px; line-height: 22.6px; }
  .doubling-table td.amount { text-align: right; }
  .doubling-table tbody tr:nth-child(even) td { background: var(--mint); }

  .rate-4 { left: 108px; width: 158px; }
  .rate-6 { left: 290px; width: 157px; }
  .rate-8 { left: 472px; width: 166px; }
  .rate-12 { left: 664px; width: 156px; }

  .doubling-note {
    position: absolute; top: 316px; border-top: 2px solid var(--leaf);
    padding-top: 10px; text-align: center; font-size: 16px; line-height: 19px;
  }
  .doubling-note strong { font-weight: 700; }

  .section-title {
    position: absolute; left: 108px; top: 450px;
    font-family: "Libre Baskerville", Georgia, serif; font-weight: 700;
    font-size: 33px; color: var(--forest);
  }

  .plan-house { position: absolute; left: 108px; top: 520px; width: 703px; height: 396px; }
  .plan-house svg.roof { position: absolute; left: 0; top: 0; }
  .brand-name {
    position: absolute; left: 0; width: 703px; top: 36px; text-align: center;
    color: var(--paper); font-weight: 700; font-size: 18px;
  }
  .brand-name .dot {
    display: inline-block; width: 10px; height: 10px; border-radius: 50%;
    background: var(--brand-green); margin-right: 7px; vertical-align: 1px;
  }
  .pillars {
    position: absolute; left: 0; top: 99px; width: 703px; height: 209px;
    background: var(--mint); display: flex;
  }
  .pillar { flex: 1; position: relative; text-align: center; font-size: 13px; line-height: 17px; }
  .pillar + .pillar::before {
    content: ""; position: absolute; left: -1.5px; top: 13px; width: 3px; height: 183px;
    background: var(--brand-green); border-radius: 2px;
  }
  .pillar h3 { font-size: 24px; font-weight: 700; color: var(--brand-green); margin-top: 9px; height: 32px; line-height: 32px; }
  .pillar ul { list-style: none; margin-top: 6px; }
  .pillar li { min-height: 34px; padding: 0 6px; }
  .pillar .outcome {
    position: absolute; left: 0; right: 0; bottom: 11px;
    color: var(--brick); font-weight: 700; font-size: 16px;
  }
  .foundation {
    position: absolute; left: 0; top: 308px; width: 703px; height: 88px;
    background: var(--night); color: var(--paper); font-weight: 700; font-size: 17px;
  }
  .foundation span { position: absolute; width: 360px; text-align: center; margin-left: -180px; }
  .foundation .rule {
    position: absolute; left: 31px; right: 31px; top: 42px; height: 2px; background: var(--brand-green);
  }

  .page-footer {
    position: absolute; left: 108px; top: 1059px; width: 704px;
    border-top: 2px solid var(--leaf); text-align: center; padding-top: 33px;
    font-family: "Libre Baskerville", Georgia, serif; font-weight: 700; font-size: 12px; color: var(--forest);
  }
</style>
</head>
<body>

<table class="doubling-table rate-4">
  <thead><tr><th>Age</th><th class="rate">4%</th></tr></thead>
  <tbody>
    <tr><td>29</td><td class="amount">$10,000</td></tr>
    <tr><td>47</td><td class="amount">$20,000</td></tr>
    <tr><td>65</td><td class="amount">$40,000</td></tr>
  </tbody>
</table>
<table class="doubling-table rate-6">
  <thead><tr><th>Age</th><th class="rate">6%</th></tr></thead>
  <tbody>
    <tr><td>29</td><td class="amount">$10,000</td></tr>
    <tr><td>41</td><td class="amount">$20,000</td></tr>
    <tr><td>53</td><td class="amount">$40,000</td></tr>
    <tr><td>65</td><td class="amount">$80,000</td></tr>
  </tbody>
</table>
<table class="doubling-table rate-8">
  <thead><tr><th>Age</th><th class="rate">8%</th></tr></thead>
  <tbody>
    <tr><td>29</td><td class="amount">$10,000</td></tr>
    <tr><td>38</td><td class="amount">$20,000</td></tr>
    <tr><td>47</td><td class="amount">$40,000</td></tr>
    <tr><td>56</td><td class="amount">$80,000</td></tr>
    <tr><td>65</td><td class="amount">$160,000</td></tr>
  </tbody>
</table>
<table class="doubling-table rate-12">
  <thead><tr><th>Age</th><th class="rate">12%</th></tr></thead>
  <tbody>
    <tr><td>29</td><td class="amount">$10,000</td></tr>
    <tr><td>35</td><td class="amount">$20,000</td></tr>
    <tr><td>41</td><td class="amount">$40,000</td></tr>
    <tr><td>47</td><td class="amount">$80,000</td></tr>
    <tr><td>53</td><td class="amount">$160,000</td></tr>
    <tr><td>59</td><td class="amount">$320,000</td></tr>
    <tr><td>65</td><td class="amount">$640,000</td></tr>
  </tbody>
</table>

<p class="doubling-note" style="left:108px;width:158px">Money double<br>every <strong>18 years</strong></p>
<p class="doubling-note" style="left:290px;width:157px">Money double<br>every <strong>12 years</strong></p>
<p class="doubling-note" style="left:472px;width:166px">Money double<br>every <strong>9 years</strong></p>
<p class="doubling-note" style="left:664px;width:156px">Money double<br>every <strong>6 years</strong></p>

<h2 class="section-title">Taxes</h2>

<section class="plan-house">
  <svg class="roof" width="703" height="99" viewBox="0 0 703 99" aria-hidden="true">
    <polygon points="0,86 351,0 703,86 703,99 0,99" fill="var(--night)"/>
  </svg>
  <p class="brand-name"><span class="dot"></span>Quillmere</p>

  <div class="pillars">
    <div class="pillar">
      <h3>HOME</h3>
      <ul>
        <li>Partner with mortgage brokers for best rates</li>
        <li>Mortgage insurance alternatives</li>
      </ul>
      <p class="outcome">SELL</p>
    </div>
    <div class="pillar">
      <h3>RRSP</h3>
      <ul>
        <li>Tax deduction</li>
        <li>Tax deferred</li>
      </ul>
      <p class="outcome">100% tax</p>
    </div>
    <div class="pillar">
      <h3>TFSA</h3>
      <ul>
        <li>No tax deductions</li>
        <li>Tax free growth</li>
        <li>2009 - $95,000</li>
        <li>Limit 2023 - $7,000/YR</li>
      </ul>
      <p class="outcome">0% tax</p>
    </div>
    <div class="pillar">
      <h3>PERM LIFE</h3>
      <ul>
        <li>No tax deduction</li>
        <li>Qualify</li>
        <li>Tax deferred growth</li>
      </ul>
      <p class="outcome">0% tax</p>
    </div>
  </div>

  <div class="foundation">
    <span style="left:179px;top:12px">Life insurance illness</span>
    <span style="left:541px;top:12px">Debt management</span>
    <div class="rule"></div>
    <span style="left:179px;top:51px">Critical / Disability</span>
    <span style="left:541px;top:51px">Cash flow</span>
  </div>
</section>

<footer class="page-footer">www.quillmereplans.ca</footer>

</body>
</html>
```